Re-design my 1-page website to be BETTER!

Hi Guys,
I recently created a 1-page website for market testing purposes for a company I am starting. Problem is, the feedback i've had on the page is its a bit corporate and boring.
I would love you to design something that is fresher, more modern and will generate leads (via the sign up CTA's).
Here is the website as it is now: www.guidelinkhub.com.au.
If you need any info or have questions, just reach out.
Thanks,
Oliver

Target Market(s)

Entrepreneurs

Number of Pages Required

1 page

Font styles to use
Sans Serif

Colors
abd036
34a6d7
ffffff

Requirements
Must have
• Fresh, Modern, high-converting
• I expect 70% of traffic to be mobile so must be mobile optimised first.
Nice to have
• I've highlighted colours i like below, however, I am open to suggestions. I like colours that are gender neutral and show energy and vibrancy.
• I have used Proxima Nova for the fonts, as I find it easy to read however, I am open to suggestions. My main preference is that it displays well and is easily read

```html
<!DOCTYPE html>
<html lang="en">
<head>
<meta charset="utf-8">
<title>Guidelink Hub — A Mentor For Everyone</title>
<link href="https://fonts.googleapis.com/css2?family=Lato:wght@400;700&display=swap" rel="stylesheet">
<style>
:root{
  --blue:#2f9ad6;
  --green:#9cc83a;
  --green-btn:#95c32a;
  --ink:#2a2a2a;
  --body:#3d3d3d;
  --grey:#ececec;
  --stage:#262626;
  --white:#ffffff;
  --band:linear-gradient(100deg,#2f95d3 0%,#46aab2 30%,#7dbf52 62%,#9dcb31 100%);
  --tile:linear-gradient(180deg,#9cc93a 0%,#6fb86a 55%,#3c9dcc 100%);
}
*{box-sizing:border-box;margin:0;padding:0}
html,body{width:1200px;height:2161px;overflow:hidden}
body{background:var(--stage);font-family:'Lato',sans-serif;color:var(--body);position:relative}
.abs{position:absolute}
.center{text-align:center}

/* ---------- desktop layout ---------- */
.desktop{position:absolute;left:50px;top:40px;width:780px;height:2081px;background:var(--white);overflow:hidden}
.brand{font-weight:700;color:var(--blue);letter-spacing:.3px;line-height:1}
.brand-tag{font-size:8px;color:var(--ink);font-weight:700;line-height:1}
.desktop .brand{left:47px;top:22px;font-size:17px}
.desktop .brand-tag{left:68px;top:44px}
.main-nav{right:47px;top:32px;display:flex;gap:24px;font-size:9px;font-weight:700;color:var(--ink);letter-spacing:.3px}
.main-nav .active{color:var(--blue)}
.hero-photo{left:0;top:68px;width:780px;height:406px;background:linear-gradient(120deg,#5b6f86 0%,#8b9db2 35%,#c9d3dc 60%,#eef1f3 100%);clip-path:polygon(0 0,100% 0,100% 100%,0 90%)}
.hero-title{font-weight:400;color:var(--blue);line-height:1}
.desktop .hero-title{right:48px;top:194px;font-size:42px}
.hero-sub{color:var(--green);line-height:1}
.desktop .hero-sub{right:112px;top:240px;font-size:16px}
.section-title{font-weight:700;color:var(--ink);line-height:1.2}
.desktop .intro-title{left:0;width:780px;top:505px;font-size:24px}
.copy{font-size:9.5px;line-height:1.75;color:var(--body)}
.desktop .intro-copy{left:118px;width:544px;top:546px}
.desktop .intro-copy p+p{margin-top:3px}
.btn{display:flex;align-items:center;justify-content:center;background:var(--green-btn);color:var(--white);font-weight:700}
.desktop .btn{width:136px;height:31px;font-size:10.5px}
.desktop .btn-start{left:322px;top:635px}
.band{background:var(--band)}
.desktop .band-diff{left:0;top:712px;width:780px;height:346px;clip-path:polygon(0 0,100% 12.5%,100% 100%,0 93%)}
.band-title{color:var(--white);font-weight:700;line-height:1.2}
.band-copy{color:var(--white);line-height:1.5}
.desktop .diff-title{left:0;width:780px;top:784px;font-size:21px}
.desktop .diff-copy{left:0;width:780px;top:817px;font-size:10px}
.step-card{background:var(--white);border:1px solid #dcdcdc;border-radius:7px;text-align:center}
.step-title{color:var(--blue);font-weight:700}
.step-copy{color:var(--body)}
.desktop .step-card{top:874px;width:213px;height:216px;padding:38px 18px 0}
.desktop .step-title{font-size:13px;margin:10px 0 5px}
.desktop .step-copy{font-size:8.5px;line-height:1.8}
.line-icon{display:block;margin:0 auto}
.desktop .growth-title{left:0;width:780px;top:1135px;font-size:21px}
.tile{background:var(--tile);border-radius:5px;color:var(--white);text-align:center}
.desktop .tile{top:1187px;width:154px;height:189px;padding:22px 12px 0}
.tile-title{font-weight:700}
.desktop .tile-title{font-size:12.5px;margin:10px 0 7px}
.desktop .tile-copy{font-size:9.2px;line-height:1.8}
.tile-icon{display:block;margin:0 auto}
.icon-person{width:40px;height:40px;margin:0 auto;background:rgba(255,255,255,.9);border-radius:6px}
.arrow{color:#6b6b6b;font-size:20px;line-height:1}
.faq-bg{background:var(--grey)}
.desktop .faq-bg{left:0;top:1426px;width:780px;height:340px;clip-path:polygon(0 0,100% 12%,100% 100%,0 100%)}
.desktop .faq-title{left:0;width:780px;top:1493px;font-size:21px}
.faq-item{background:var(--white);border:1px solid #d8d8d8;color:var(--blue);display:flex;justify-content:space-between;align-items:center}
.desktop .faq-item{height:29px;width:275px;padding:0 10px;font-size:10px}
.faq-item .chev{font-size:11px}
.faq-open{display:block;padding-top:6px}
.faq-open .row{display:flex;justify-content:space-between}
.faq-answer{color:var(--body);font-size:7.5px;line-height:1.55;margin-top:3px}
.desktop .band-cta{left:0;top:1703px;width:780px;height:259px;clip-path:polygon(0 0,100% 14%,100% 100%,0 84.5%)}
.desktop .cta-title{left:0;width:780px;top:1770px;font-size:23px}
.desktop .cta-copy{left:140px;width:500px;top:1808px;font-size:10px;line-height:2}
.desktop .btn-cta{left:322px;top:1861px}
.foot-nav{display:flex;justify-content:center;font-weight:700;color:var(--ink)}
.desktop .foot-nav{left:0;width:780px;top:1983px;gap:24px;font-size:9px}
.copyright{color:var(--ink)}
.desktop .copyright{left:0;width:780px;top:2007px;font-size:8px}
.social{display:flex;justify-content:center}
.social span{background:#333;border-radius:50%}
.desktop .social{left:0;width:780px;top:2027px;gap:14px}
.desktop .social span{width:13px;height:13px}

/* ---------- mobile layout ---------- */
.mobile{position:absolute;left:893px;top:82px;width:248px;height:1995px;background:var(--white);overflow:hidden}
.mobile .brand{left:0;width:248px;top:15px;font-size:16px;text-align:center}
.mobile .brand-tag{left:0;width:248px;top:35px;text-align:center;font-size:7.5px}
.menu-btn{left:115px;top:57px;width:19px;height:17px;background:var(--green-btn);border-radius:2px;display:flex;flex-direction:column;justify-content:center;align-items:center;gap:2px}
.menu-btn i{display:block;width:9px;height:1.5px;background:var(--white)}
.mobile .hero-photo{top:84px;width:248px;height:130px;clip-path:polygon(0 0,100% 0,100% 100%,0 88%)}
.mobile .hero-title{left:0;width:248px;text-align:center;top:120px;font-size:24px}
.mobile .hero-sub{left:0;width:248px;text-align:center;top:148px;font-size:13px}
.mobile .intro-title{left:15px;width:218px;top:224px;font-size:14.5px}
.mobile .copy{font-size:8.6px;line-height:1.72}
.mobile .intro-copy{left:12px;width:224px;top:270px}
.mobile .btn{width:106px;height:23px;font-size:8px}
.mobile .btn-start{left:71px;top:409px}
.mobile .band-diff{left:0;top:458px;width:248px;height:210px;clip-path:polygon(0 0,100% 14%,100% 54%,0 68%)}
.mobile .diff-title{left:0;width:248px;top:494px;font-size:13.5px}
.mobile .diff-copy{left:22px;width:204px;top:515px;font-size:8.2px;line-height:1.45}
.mobile .step-card{left:33px;width:182px;height:182px;padding:30px 12px 0}
.mobile .step-title{font-size:11px;margin:8px 0 5px}
.mobile .step-copy{font-size:7.4px;line-height:1.85}
.mobile .growth-title{left:10px;width:228px;top:1158px;font-size:14px}
.mobile .tile{left:45px;top:1201px;width:155px;height:189px;padding:22px 13px 0}
.mobile .tile-title{font-size:13px;margin:10px 0 6px}
.mobile .tile-copy{font-size:8.8px;line-height:1.8}
.mobile .faq-bg{left:0;top:1410px;width:248px;height:300px;clip-path:polygon(0 0,100% 7%,100% 100%,0 100%)}
.mobile .faq-title{left:0;width:248px;top:1442px;font-size:14px}
.mobile .faq-item{left:12px;width:223px;height:22px;padding:0 8px;font-size:8.4px}
.mobile .band-cta{left:0;top:1700px;width:248px;height:180px;clip-path:polygon(0 0,100% 10%,100% 100%,0 100%)}
.mobile .cta-title{left:0;width:248px;top:1733px;font-size:14.5px}
.mobile .cta-copy{left:8px;width:232px;top:1760px;font-size:8.2px;line-height:1.8}
.mobile .btn-cta{left:71px;top:1828px}
.mobile .foot-nav{left:30px;width:188px;top:1898px;flex-wrap:wrap;gap:7px 22px;font-size:7.5px}
.mobile .copyright{left:0;width:248px;top:1940px;font-size:7.4px}
.mobile .social{left:0;width:248px;top:1960px;gap:12px}
.mobile .social span{width:12px;height:12px}
</style>
</head>
<body>

<main class="desktop" aria-label="Desktop layout">
  <div class="abs brand">Guidelink Hub</div>
  <div class="abs brand-tag">A Mentor For Everyone</div>
  <nav class="abs main-nav"><span class="active">HOME</span><span>ABOUT US</span><span>SERVICES</span><span>FAQ</span><span>BLOG</span><span>CONTACT</span></nav>

  <div class="abs hero-photo" role="img" aria-label="Photo of a smiling businessman in glasses pointing at a tablet during a meeting"></div>
  <h1 class="abs hero-title">Guidelink Hub</h1>
  <div class="abs hero-sub">A Mentor For Everyone</div>

  <h2 class="abs section-title intro-title center">Finding a Mentor Has Never Been Easier</h2>
  <div class="abs copy intro-copy center">
    <p>Having a great Mentor will turbo-charge your personal, professional or business growth.&nbsp; But unless you have an incredible network, finding great Mentors has always been a challenge.</p>
    <p>Guidelink Hub changes all that, levelling the playing field and making it easy for entrepreneurs and professionals to find the advice and guidance they deserve.</p>
  </div>
  <a class="abs btn btn-start">Let's Get Started</a>

  <div class="abs band band-diff"></div>
  <h2 class="abs band-title diff-title center">Mentorship: But Different</h2>
  <p class="abs band-copy diff-copy center">Finding a Mentor used to be hard; but not any more.<br>We've turned the traditional model on its head, so now Mentors seek you.</p>

  <div class="abs step-card" style="left:49px">
    <svg class="line-icon" width="42" height="50" viewBox="0 0 42 50" fill="none" stroke-width="1.6"><path d="M4 2h24l10 10v36H4z" stroke="#2f9ad6"/><path d="M28 2v10h10" stroke="#2f9ad6"/><rect x="11" y="22" width="20" height="6" stroke="#9cc83a"/><rect x="11" y="30" width="20" height="6" stroke="#9cc83a"/><rect x="11" y="38" width="20" height="6" stroke="#9cc83a"/></svg>
    <div class="step-title">Tell Us What You Need</div>
    <p class="step-copy">There is no one size fits all approach to Mentorship.&nbsp; So tell us the challenges you are facing and the skill-set your Mentor must have.</p>
  </div>
  <div class="abs step-card" style="left:284px">
    <svg class="line-icon" width="50" height="50" viewBox="0 0 50 50" fill="none" stroke-width="1.6"><circle cx="13" cy="14" r="6" stroke="#9cc83a"/><circle cx="37" cy="14" r="6" stroke="#9cc83a"/><circle cx="25" cy="24" r="7" stroke="#2f9ad6"/><path d="M10 46c0-9 7-13 15-13s15 4 15 13z" stroke="#2f9ad6"/><path d="M3 34c0-7 4-11 10-11M47 34c0-7-4-11-10-11" stroke="#9cc83a"/></svg>
    <div class="step-title">Choose Your Mentor</div>
    <p class="step-copy">Mentors are invited to Mentor you.<br>We select 3 top picks that align with your criteria. It's then up to you whether you choose a Mentor..</p>
  </div>
  <div class="abs step-card" style="left:506px">
    <svg class="line-icon" width="56" height="50" viewBox="0 0 56 50" fill="none" stroke-width="1.6"><path d="M3 18c0-8 8-14 19-14s19 6 19 14-8 14-19 14c-3 0-5 0-7-1l-9 5 3-7c-4-3-6-6-6-11z" stroke="#9cc83a"/><path d="M44 20c6 2 10 7 10 12 0 4-2 7-5 9l2 6-8-4c-2 1-4 1-6 1-7 0-13-3-15-8" stroke="#2f9ad6"/></svg>
    <div class="step-title">Ongoing Support</div>
    <p class="step-copy">We don't stop once you have your perfect Mentor.&nbsp; We're on hand to make life easy for you, keep your sessions on track and provide ongoing support.</p>
  </div>

  <h2 class="abs section-title growth-title center">How a Mentor Will Accelerate Your Growth</h2>
  <div class="abs arrow" style="left:28px;top:1271px">&#8249;</div>
  <div class="abs arrow" style="left:744px;top:1271px">&#8250;</div>
  <div class="abs tile" style="left:49px">
    <div class="icon-person" role="img" aria-label="Icon of an advisor with a speech bubble"></div>
    <div class="tile-title">Impartial advice</div>
    <p class="tile-copy">Imagine being able to speak to someone who has been through the challenges you are currently facing?</p>
  </div>
  <div class="abs tile" style="left:225px">
    <svg class="tile-icon" width="40" height="40" viewBox="0 0 40 40" fill="none" stroke="#fff" stroke-width="2.4"><rect x="6" y="6" width="24" height="30" rx="2"/><path d="M13 3h10v6H13z" fill="#fff"/><path d="M11 16h8M11 22h8M11 28h6"/><path d="M36 24H24M28 20l-4 4 4 4"/></svg>
    <div class="tile-title">Avoid the Pitfalls</div>
    <p class="tile-copy">Imagine being able to speak to someone who has been through the challenges you are currently facing?</p>
  </div>
  <div class="abs tile" style="left:400px">
    <div class="icon-person" role="img" aria-label="Icon of a support agent with a headset"></div>
    <div class="tile-title">A Supportive Ear</div>
    <p class="tile-copy">Imagine being able to speak to someone who has been through the challenges you are currently facing?</p>
  </div>
  <div class="abs tile" style="left:578px">
    <svg class="tile-icon" width="40" height="40" viewBox="0 0 40 40" fill="none" stroke="#fff" stroke-width="4"><circle cx="16" cy="16" r="10"/><path d="M24 24l11 11" stroke-linecap="round"/></svg>
    <div class="tile-title">Clarity</div>
    <p class="tile-copy">Imagine being able to speak to someone who has been through the challenges you are currently facing?</p>
  </div>

  <div class="abs faq-bg"></div>
  <h2 class="abs section-title faq-title center">Frequently Asked Questions</h2>
  <div class="abs faq-item" style="left:107px;top:1542px"><span>What is a Mentor?</span><span class="chev">&raquo;</span></div>
  <div class="abs faq-item" style="left:107px;top:1578px"><span>Is a Mentor right for me?</span><span class="chev">&raquo;</span></div>
  <div class="abs faq-item faq-open" style="left:107px;top:1613px;height:65px">
    <div class="row"><span>How often do we meet?</span><span class="chev">&#8744;</span></div>
    <p class="faq-answer">How often you meet your Mentor is entirely up to you and something you should discuss and agree with your Mentor.</p>
  </div>
  <div class="abs faq-item" style="left:400px;top:1542px"><span>Can I have more than one Mentor?</span><span class="chev">&raquo;</span></div>
  <div class="abs faq-item" style="left:400px;top:1578px"><span>What if it doesn't work out?</span><span class="chev">&raquo;</span></div>
  <div class="abs faq-item" style="left:400px;top:1613px"><span>How do we meet?</span><span class="chev">&raquo;</span></div>
  <div class="abs faq-item" style="left:400px;top:1649px"><span>What are the costs?</span><span class="chev">&raquo;</span></div>

  <div class="abs band band-cta"></div>
  <h2 class="abs band-title cta-title center">It's Time to Invest in You</h2>
  <p class="abs band-copy cta-copy center">If you've come this far you've already taken the most important step: recognising how mentorship can help you; and taking action to find it. And now your here, the rest is easy.</p>
  <a class="abs btn btn-cta">Let's Do This</a>

  <nav class="abs foot-nav"><span>HOME</span><span>ABOUT US</span><span>SERVICES</span><span>FAQ</span><span>BLOG</span><span>CONTACT</span></nav>
  <p class="abs copyright center">Copyright &copy;2018&nbsp; Company Name. All Rights Reserved</p>
  <div class="abs social" aria-label="Social links"><span></span><span></span><span></span><span></span><span></span></div>
</main>

<main class="mobile" aria-label="Mobile layout">
  <div class="abs brand">Guidelink Hub</div>
  <div class="abs brand-tag">A Mentor For Everyone</div>
  <div class="abs menu-btn" aria-label="Menu"><i></i><i></i><i></i></div>

  <div class="abs hero-photo" role="img" aria-label="Photo of a smiling businessman in glasses pointing at a tablet during a meeting"></div>
  <h1 class="abs hero-title">Guidelink Hub</h1>
  <div class="abs hero-sub">A Mentor For Everyone</div>

  <h2 class="abs section-title intro-title center">Finding a Mentor Has Never Been Easier</h2>
  <div class="abs copy intro-copy center">
    <p>Having a great Mentor will turbo-charge your personal, professional or business growth.</p>
    <p>But unless you have an incredible network, finding great Mentors has always been a challenge. Guidelink Hub changes all that, levelling the playing field and making it easy for entrepreneurs and professionals to find the advice and guidance they deserve.</p>
  </div>
  <a class="abs btn btn-start">Let's Get Started</a>

  <div class="abs band band-diff"></div>
  <h2 class="abs band-title diff-title center">Mentorship: But Different</h2>
  <p class="abs band-copy diff-copy center">Finding a Mentor used to be hard; but not any more. We've turned the traditional model on its head, so now Mentors seek you.</p>

  <div class="abs step-card" style="top:569px">
    <svg class="line-icon" width="34" height="40" viewBox="0 0 42 50" fill="none" stroke-width="1.8"><path d="M4 2h24l10 10v36H4z" stroke="#2f9ad6"/><path d="M28 2v10h10" stroke="#2f9ad6"/><rect x="11" y="22" width="20" height="6" stroke="#9cc83a"/><rect x="11" y="30" width="20" height="6" stroke="#9cc83a"/><rect x="11" y="38" width="20" height="6" stroke="#9cc83a"/></svg>
    <div class="step-title">Tell Us What You Need</div>
    <p class="step-copy">There is no one size fits all approach to Mentorship.&nbsp; So tell us the challenges you are facing and the skill-set your Mentor must have.</p>
  </div>
  <div class="abs step-card" style="top:760px">
    <svg class="line-icon" width="40" height="40" viewBox="0 0 50 50" fill="none" stroke-width="1.8"><circle cx="13" cy="14" r="6" stroke="#9cc83a"/><circle cx="37" cy="14" r="6" stroke="#9cc83a"/><circle cx="25" cy="24" r="7" stroke="#2f9ad6"/><path d="M10 46c0-9 7-13 15-13s15 4 15 13z" stroke="#2f9ad6"/><path d="M3 34c0-7 4-11 10-11M47 34c0-7-4-11-10-11" stroke="#9cc83a"/></svg>
    <div class="step-title">Choose Your Mentor</div>
    <p class="step-copy">Mentors are invited to Mentor you.<br>We select 3 top picks that align with your criteria. It's then up to you whether you choose a Mentor..</p>
  </div>
  <div class="abs step-card" style="top:950px">
    <svg class="line-icon" width="44" height="40" viewBox="0 0 56 50" fill="none" stroke-width="1.8"><path d="M3 18c0-8 8-14 19-14s19 6 19 14-8 14-19 14c-3 0-5 0-7-1l-9 5 3-7c-4-3-6-6-6-11z" stroke="#9cc83a"/><path d="M44 20c6 2 10 7 10 12 0 4-2 7-5 9l2 6-8-4c-2 1-4 1-6 1-7 0-13-3-15-8" stroke="#2f9ad6"/></svg>
    <div class="step-title">Ongoing Support</div>
    <p class="step-copy">We don't stop once you have your perfect Mentor.&nbsp; We're on hand to make life easy for you, keep your sessions on track and provide ongoing support.</p>
  </div>

  <h2 class="abs section-title growth-title center">How a Mentor Will Accelerate Your Growth</h2>
  <div class="abs arrow" style="left:22px;top:1283px">&#8249;</div>
  <div class="abs arrow" style="left:216px;top:1283px">&#8250;</div>
  <div class="abs tile">
    <div class="icon-person" role="img" aria-label="Icon of an advisor with a speech bubble"></div>
    <div class="tile-title">Impartial advice</div>
    <p class="tile-copy">Imagine being able to speak to someone who has been through the challenges you are currently facing?</p>
  </div>

  <div class="abs faq-bg"></div>
  <h2 class="abs section-title faq-title center">Frequently Asked Questions</h2>
  <div class="abs faq-item" style="top:1473px"><span>What is a Mentor?</span><span class="chev">&raquo;</span></div>
  <div class="abs faq-item" style="top:1502px"><span>Is a Mentor right for me?</span><span class="chev">&raquo;</span></div>
  <div class="abs faq-item" style="top:1532px"><span>How often do we meet?</span><span class="chev">&raquo;</span></div>
  <div class="abs faq-item" style="top:1561px"><span>Can I have more than one Mentor?</span><span class="chev">&raquo;</span></div>
  <div class="abs faq-item" style="top:1591px"><span>What if it doesn't work out?</span><span class="chev">&raquo;</span></div>
  <div class="abs faq-item" style="top:1620px"><span>How do we meet?</span><span class="chev">&raquo;</span></div>
  <div class="abs faq-item" style="top:1650px"><span>What are the costs?</span><span class="chev">&raquo;</span></div>

  <div class="abs band band-cta"></div>
  <h2 class="abs band-title cta-title center">It's Time to Invest in You</h2>
  <p class="abs band-copy cta-copy center">If you've come this far you've already taken the most important step: recognising how mentorship can help you; and taking action to find it. And now your here, the rest is easy.</p>
  <a class="abs btn btn-cta">Let's Do This</a>

  <nav class="abs foot-nav"><span>HOME</span><span>ABOUT US</span><span>SERVICES</span><span>FAQ</span><span>BLOG</span><span>CONTACT</span></nav>
  <p class="abs copyright center">Copyright &copy;2018&nbsp; Company Name. All Rights Reserved</p>
  <div class="abs social" aria-label="Social links"><span></span><span></span><span></span><span></span><span></span></div>
</main>

</body>
</html>
```